WordPress Website for Pain Relief Clinic

I need a WordPress website designed for my laser pain relief clinic. It needs to be a professional, responsive design with 7 pages: Home, Why Choose Us, Treatable Conditions, Testimonials, FAQ, Franchising, Contact Us. Here is logo: https://files.brivoltcdn.com/media.t-w-e-n.com/sitebuilder/472/CalvexaLogoHighQuality.png

Target Market(s)

people with pain,elderly adults,injuries,soreness

Industry/Entity Type

Clinic

Number of Pages Required

5+ page

Colors
0792cd
85abd2

```html
<!DOCTYPE html>
<html lang="en">
<head>
<meta charset="utf-8">
<title>Calvexa Pain Treatment Center</title>
<link href="https://fonts.googleapis.com/css2?family=Roboto:wght@300;400;500;700&display=swap" rel="stylesheet">
<style>
  :root{
    --brand:#0792cd;
    --brand-soft:#85abd2;
    --band:#1b8fd3;
    --accent-red:#d9262c;
    --ink:#333;
    --muted:#666;
    --light:#f2f2f2;
    --footer:#1d1d1d;
    --footer-2:#141414;
  }
  *{box-sizing:border-box;margin:0;padding:0}
  html,body{width:713px;height:1200px;overflow:hidden;background:#fff}
  body{font-family:"Roboto",Arial,sans-serif;color:var(--ink);position:relative}
  .abs{position:absolute}
  /* top bar */
  .topbar{top:0;left:0;width:713px;height:33px;border-bottom:1px solid #e6e6e6}
  .topbar .contact{top:9px;font-size:11px;color:var(--brand);display:flex;align-items:center;gap:5px}
  .topbar .social{top:9px;right:20px;display:flex;gap:22px}
  .dot{width:12px;height:12px;border-radius:50%;background:var(--brand-soft);display:block}
  /* header */
  .brand{top:38px;left:0;width:713px;text-align:center}
  .brand .name{font-size:40px;font-weight:700;color:var(--brand);letter-spacing:1px;line-height:44px}
  .brand .tag{font-size:9px;color:var(--muted);letter-spacing:2px;text-transform:uppercase}
  /* nav */
  .nav{top:95px;left:0;width:713px;height:29px;background:#fff;border-top:1px solid #e6e6e6;display:flex;padding-left:48px;font-size:11px}
  .nav a{color:var(--muted);text-decoration:none;padding:0 10px;line-height:28px}
  .nav a.active{background:var(--accent-red);color:#fff}
  /* hero */
  .hero{top:124px;left:0;width:713px;height:286px;background:linear-gradient(180deg,#f7f7f7,#e9ebec)}
  .hero-photos{top:6px;left:20px}
  .hero h1{top:62px;left:410px;width:280px;text-align:right;font-weight:400;font-size:31px;line-height:34px;color:#444}
  .hero p{top:140px;left:420px;width:265px;font-size:9px;line-height:13px;color:var(--muted)}
  .btn{display:inline-block;background:var(--band);color:#fff;font-size:12px;padding:0 12px;line-height:28px;font-weight:500}
  .hero .btn{top:172px;left:602px}
  .pager{top:262px;left:334px;display:flex;gap:6px}
  .pager i{width:8px;height:8px;border-radius:50%;border:1px solid #aaa;display:block}
  /* call band */
  .callband{top:410px;left:0;width:713px;height:125px;background:var(--band);color:#fff;text-align:center}
  .callband h2{font-weight:400;font-size:27px;margin-top:30px}
  .callband .phone{font-size:31px;margin-top:8px}
  /* why */
  .why{top:535px;left:0;width:713px;height:295px;text-align:center}
  .why h2{font-weight:400;font-size:29px;color:var(--brand);margin-top:108px}
  .why p{width:430px;margin:24px auto 0;font-size:9px;line-height:13px;color:var(--muted)}
  .why p + p{margin-top:14px}
  .why .btn{margin-top:14px}
  /* testimonial */
  .testimonial{top:830px;left:0;width:713px;height:242px;background:linear-gradient(180deg,#e4e5e3,#cfd2cf);text-align:center}
  .testimonial h2{font-weight:400;font-size:28px;color:#333;margin-top:30px}
  .testimonial .quote{font-size:38px;line-height:30px;color:#333;margin-top:10px;font-weight:700}
  .testimonial p{width:440px;margin:6px auto 0;font-size:9px;line-height:13px;color:#444}
  .testimonial .who{font-size:9px;margin-top:22px;font-weight:500}
  .arrow{top:112px}
  /* footer */
  .footnav{top:1072px;left:0;width:713px;height:33px;background:var(--footer);display:flex;align-items:center;padding-left:48px;font-size:11px}
  .footnav a{color:#fff;text-decoration:none;padding:0 8px}
  .footnav a.active{border:1px solid #fff;border-radius:12px;padding:2px 12px}
  .footnav .social{display:flex;gap:20px;margin-left:18px}
  .footinfo{top:1105px;left:0;width:713px;height:95px;background:var(--footer-2);color:#ddd;font-size:10px}
  .info-item{top:18px;display:flex;align-items:center;gap:10px}
  .ico{width:28px;height:28px;border-radius:50%;background:var(--band);display:flex;align-items:center;justify-content:center;flex:none}
  .copy{top:70px;left:0;width:713px;text-align:center;font-size:9px;color:#aaa}
  .copy b{color:var(--brand);font-weight:400}
</style>
</head>
<body>

<header class="topbar abs">
  <div class="contact abs" style="left:48px">
    <svg width="11" height="11" viewBox="0 0 24 24"><path fill="#0792cd" d="M6.6 10.8a15 15 0 006.6 6.6l2.2-2.2c.3-.3.7-.4 1-.2 1.1.4 2.3.6 3.6.6.6 0 1 .4 1 1V20c0 .6-.4 1-1 1C10.6 21 3 13.4 3 4c0-.6.4-1 1-1h3.5c.6 0 1 .4 1 1 0 1.3.2 2.5.6 3.6.1.3 0 .7-.2 1z"/></svg>
    123 456 7890
  </div>
  <div class="contact abs" style="left:185px">
    <svg width="12" height="10" viewBox="0 0 24 18"><rect x="1" y="1" width="22" height="16" rx="2" fill="none" stroke="#0792cd" stroke-width="2"/><path d="M1 2l11 8 11-8" fill="none" stroke="#0792cd" stroke-width="2"/></svg>
    info@calvexaclinic.com
  </div>
  <div class="social abs"><span class="dot"></span><span class="dot"></span><span class="dot"></span></div>
</header>

<div class="brand abs">
  <div class="name">Calvexa</div>
  <div class="tag">Pain Treatment Center</div>
</div>

<nav class="nav abs">
  <a class="active">Home</a><a>Why Choose Us</a><a>Treatable Conditions</a><a>Testimonials</a><a>FAQ</a><a>Franchising</a><a>Contact Us</a>
</nav>

<section class="hero abs">
  <svg class="hero-photos abs" width="330" height="270" role="img" aria-label="Collage of round photos showing laser treatment on painful joints">
    <g fill="#e8d2c6" stroke="#fff" stroke-width="3">
      <circle cx="175" cy="120" r="78" fill="#d7e3ea"/>
      <circle cx="60" cy="62" r="45"/>
      <circle cx="135" cy="30" r="32"/>
      <circle cx="265" cy="48" r="46"/>
      <circle cx="42" cy="165" r="40"/>
      <circle cx="110" cy="225" r="40"/>
      <circle cx="215" cy="228" r="38"/>
      <circle cx="290" cy="160" r="38"/>
    </g>
  </svg>
  <h1 class="abs">Recover with<br>Laser Solutions</h1>
  <p class="abs">Lorem Ipsum is simply dummy text of the printing and typesetting industry. Lorem Ipsum has been the industry's standard dummy text ever since the 1500s</p>
  <a class="btn abs">READ MORE</a>
  <div class="pager abs"><i></i><i></i><i></i></div>
</section>

<section class="callband abs">
  <h2>Start Living Pain Free Today</h2>
  <div class="phone">Call us - 123 456 7890</div>
</section>

<section class="why abs">
  <h2>Why Choose Us</h2>
  <p>Lorem Ipsum is simply dummy text of the printing and typesetting industry. Lorem Ipsum has been the industry's standard dummy text ever since the 1500s, when an unknown printer took a galley of type and scrambled it to make a type specimen book. It has survived not only five centuries, but also the leap into electronic typesetting, remaining essentially unchanged.</p>
  <p>Lorem Ipsum is simply dummy text of the printing and typesetting industry. Lorem Ipsum has been the industry's standard dummy text ever since the 1500s</p>
  <a class="btn">READ MORE</a>
</section>

<section class="testimonial abs" role="img" aria-label="Soft background photo of a clinic treatment room">
  <h2>Our Client Say</h2>
  <div class="quote">&ldquo;</div>
  <p>Lorem Ipsum is simply dummy text of the printing and typesetting industry. Lorem Ipsum has been the industry's standard dummy text ever since the 1500s, when an unknown printer took a galley of type and scrambled it to make a type specimen book. It has survived not only five centuries.</p>
  <div class="who">- Client Name</div>
  <svg class="arrow abs" style="left:60px" width="12" height="24"><path d="M10 2L2 12l8 10" fill="none" stroke="#333" stroke-width="2"/></svg>
  <svg class="arrow abs" style="right:60px" width="12" height="24"><path d="M2 2l8 10-8 10" fill="none" stroke="#333" stroke-width="2"/></svg>
</section>

<nav class="footnav abs">
  <a class="active">Home</a><a>Why Choose Us</a><a>Treatable Conditions</a><a>Testimonials</a><a>FAQ</a><a>Franchising</a><a>Contact Us</a>
  <span class="social"><span class="dot"></span><span class="dot"></span><span class="dot"></span></span>
</nav>

<footer class="footinfo abs">
  <div class="info-item abs" style="left:48px;width:200px">
    <span class="ico"><svg width="12" height="14" viewBox="0 0 24 28"><path fill="#fff" d="M12 0a10 10 0 00-10 10c0 7.5 10 18 10 18s10-10.5 10-18A10 10 0 0012 0zm0 14a4 4 0 110-8 4 4 0 010 8z"/></svg></span>
    <span>Lorem Ipsum is simply dummy text of the printing and typesetting</span>
  </div>
  <div class="info-item abs" style="left:310px">
    <span class="ico"><svg width="13" height="13" viewBox="0 0 24 24"><path fill="#fff" d="M6.6 10.8a15 15 0 006.6 6.6l2.2-2.2c.3-.3.7-.4 1-.2 1.1.4 2.3.6 3.6.6.6 0 1 .4 1 1V20c0 .6-.4 1-1 1C10.6 21 3 13.4 3 4c0-.6.4-1 1-1h3.5c.6 0 1 .4 1 1 0 1.3.2 2.5.6 3.6.1.3 0 .7-.2 1z"/></svg></span>
    <span>123 456 7890</span>
  </div>
  <div class="info-item abs" style="left:488px">
    <span class="ico"><svg width="13" height="10" viewBox="0 0 24 18"><rect x="1" y="1" width="22" height="16" rx="2" fill="none" stroke="#fff" stroke-width="2"/><path d="M1 2l11 8 11-8" fill="none" stroke="#fff" stroke-width="2"/></svg></span>
    <span>info@calvexapaintreatment.com</span>
  </div>
  <div class="copy abs">&copy; <b>Calvexa Pain Treatment Limited</b> - 2016, All Rights reserved.</div>
</footer>

</body>
</html>
```